Need Amazing Website for Consulting Company

We need an amazing website design for a Human Resources Consulting Company. This will be geared towards a more professional crowd, but we don't want it to be overly corporate and stuffy: Just, clean and professional and amazing. Please use the video link below for further instruction.

http://clipvarn.example/t/kzQmPoLe7

Thank You.

PS Logo file has been attached.

Target Market(s)

The target marketing is small business owners who have employees. These owners cant afford an in-house HR person so they would hire this client to consult and do the work for them.

Industry/Entity Type

It Company

Font styles to use
Sans Serif

Requirements
Must have
• Please watch video:

Must have spot for video on homepage.
Nice to have
• Clean, professional, but not overly corporate, we want a personal and fun feel to this site a bit to separate them from all the other executive type sites. This site should have some LIFE to it and reflect a local brand that is doing great things.
Should not have
• Should not be just a corporate site, should not be overly stuffy, should not be overly boring.

```html
<!DOCTYPE html>
<html lang="en">
<head>
<meta charset="utf-8">
<title>Mesa Ridge HR Consulting, LLC</title>
<link href="https://fonts.googleapis.com/css2?family=Lato:wght@400;700;900&family=Raleway:wght@400&display=swap" rel="stylesheet">
<style>
:root{
  --red:#c41f30;
  --red-dark:#a9172a;
  --ink:#222;
  --body:#3a3a3a;
  --panel:#1e1e1e;
  --footer:#2a2a2a;
  --grey-band:#e4e4e4;
  --white:#fff;
  --line:#444;
}
*{margin:0;padding:0;box-sizing:border-box}
html,body{width:1200px;height:1118px;overflow:hidden}
body{position:relative;background:var(--white);font-family:'Lato',sans-serif;color:var(--body)}
.abs{position:absolute}

/* header */
.brand{left:213px;top:14px;width:260px;height:66px;display:flex;align-items:center;gap:10px}
.brand-mark{width:22px;height:22px;border-radius:50%;background:var(--red);flex:none}
.brand-name{font-weight:900;font-size:17px;line-height:1.15;color:var(--ink)}

.main-nav{left:0;top:92px;width:1200px;height:39px;background:linear-gradient(#cc2637,var(--red-dark));display:flex;justify-content:center;align-items:center}
.main-nav a{color:var(--white);text-decoration:none;font-weight:700;font-size:12px;letter-spacing:1.1px;white-space:nowrap}
.main-nav .sep{color:var(--white);font-size:11px;margin:0 12px}

/* hero */
.hero{left:0;top:131px;width:1200px;height:297px;background:linear-gradient(100deg,#cfcac3 0%,#a9a49d 20%,#dcdad6 45%,#c9ccd0 70%,#3a6f9c 88%,#d8d6d2 100%)}
.video{left:213px;top:147px;width:469px;height:264px;background:linear-gradient(110deg,#f2f3f5 0%,#e4e7ec 35%,#b9c7d9 55%,#eceef1 100%);overflow:hidden}
.video-tag{right:20px;top:18px;font-family:'Raleway',sans-serif;font-size:20px;line-height:1.2;color:var(--red)}
.play-ring{left:214px;top:98px}
.video-bar{left:18px;top:220px;width:432px;height:30px}
.play-btn{left:0;top:0;width:52px;height:30px;background:#3b3b3b;border-radius:3px}
.track{left:62px;top:2px;width:370px;height:26px;background:#2f2f2f;border-radius:3px}
.track-fill{left:6px;top:10px;width:246px;height:6px;background:#555}
.track-buffer{left:0;top:0;width:76px;height:6px;background:#1e8fe0}
.hd{left:319px;top:5px;font-weight:900;font-size:12px;color:#1e8fe0}

.about-panel{left:693px;top:147px;width:293px;height:264px;background:linear-gradient(135deg,#2b2b2b,var(--panel))}
.about-title{left:17px;top:16px;white-space:nowrap;color:var(--white);font-weight:700;font-size:11.5px;letter-spacing:1.3px}
.about-rule{left:17px;top:37px;width:259px;height:1px;background:var(--red)}
.about-photo{left:19px;top:53px;width:255px;height:90px;background:linear-gradient(90deg,#f3e4d8 0%,#e9d8ca 35%,#c9d2dc 60%,#eef0f2 100%)}
.about-text{left:19px;top:150px;width:255px;color:var(--white);font-size:10px;line-height:14.5px;font-weight:700}
.about-text span{display:block;white-space:nowrap;text-align:justify;text-align-last:justify}
.about-text span:last-child{text-align-last:left}
.about-tags{left:19px;top:240px;width:255px;display:flex;justify-content:space-between;color:var(--white);font-size:12.5px;letter-spacing:.3px}
.about-tags i{font-style:normal;font-size:9px;color:#aaa;padding-top:2px}

/* features */
.feature{top:452px;width:160px;text-align:center}
.feature h3{width:240px;margin-left:-40px;white-space:nowrap;font-weight:700;font-size:11.2px;letter-spacing:1.3px;color:var(--ink)}
.feature .icon{display:block;margin:14px auto 0}
.feature p{margin-top:12px;font-size:11px;line-height:12.4px;text-align:justify;color:var(--ink)}
.feature .links{margin-top:10px;text-align:left;font-size:10.5px;line-height:22px;white-space:nowrap;color:var(--ink)}
.feature .links b{color:var(--red);font-weight:400}
.learn{display:block;margin:16px auto 0;width:70px;height:18px;border:1px dashed var(--red);border-radius:9px;font-size:6.5px;font-weight:900;letter-spacing:1px;line-height:16px;color:var(--ink);text-align:center}
.divider{top:460px;width:30px;height:120px;background:linear-gradient(90deg,rgba(0,0,0,.05),rgba(0,0,0,0))}

/* band */
.band{left:0;top:690px;width:1200px;height:179px;background:var(--grey-band)}
.quote{left:214px;top:717px;width:425px;height:123px;background:#ececec;border:1px solid #d2d2d2;box-shadow:0 2px 5px rgba(0,0,0,.18)}
.quote-photo{left:12px;top:23px;width:84px;height:83px;background:linear-gradient(#d9d4cc,#a99f93)}
.quote-text{left:105px;top:21px;width:309px;font-size:11px;line-height:12.6px;text-align:justify;color:var(--body)}
.quote-by{right:12px;top:102px;font-size:10.5px;color:var(--ink)}
.quote-by b{font-weight:700;margin-right:10px}

.clients-title{left:696px;top:716px;width:241px;text-align:center;font-weight:700;font-size:11.2px;letter-spacing:1.3px;color:var(--ink)}
.clients-box{left:696px;top:755px;width:241px;height:82px;background:#cfcfcf;padding:8px}
.clients-inner{width:100%;height:100%;background:var(--white);display:flex;align-items:center;justify-content:center;font-weight:900;font-size:17px;color:var(--ink)}
.arrow{top:779px}

.zig{left:0;top:892px;width:1200px;height:16px;background:repeating-linear-gradient(45deg,#cfcfcf 0 2px,#fff 2px 4px)}

/* footer */
.footer{left:0;top:908px;width:1200px;height:173px;background:var(--footer)}
.foot-col h4{font-weight:700;font-size:11.2px;letter-spacing:1.3px;color:var(--white)}
.foot-list{list-style:none;margin-top:19px}
.foot-list li{font-size:11px;color:var(--white);height:24px;line-height:20px;border-bottom:1px solid var(--line)}
.foot-list li:last-child{border-bottom:none}
.contact li{display:flex;gap:12px;align-items:flex-start}
.contact svg{flex:none;margin-top:4px}
.social{display:flex;gap:7px;margin-top:20px}
.social span{height:28px;min-width:28px;padding:0 7px;border-radius:5px;background:var(--white);color:var(--ink);font-size:10px;font-weight:700;display:flex;align-items:center;justify-content:center;white-space:nowrap}
.copy{left:0;top:1081px;width:1200px;height:37px;background:var(--red);color:var(--white);font-size:11px;text-align:center;line-height:37px}
</style>
</head>
<body>

<header>
  <div class="abs brand">
    <span class="brand-mark"></span>
    <span class="brand-name">Mesa Ridge HR<br>Consulting, LLC</span>
  </div>
  <nav class="abs main-nav">
    <a href="#">HOME</a><span class="sep">/</span>
    <a href="#">ETHOS</a><span class="sep">/</span>
    <a href="#">SERVICES</a><span class="sep">/</span>
    <a href="#">NEWS &amp; MEDIA</a><span class="sep">/</span>
    <a href="#">CLIENTELE</a><span class="sep">/</span>
    <a href="#">OUR UNIQUE OFFERINGS</a><span class="sep">/</span>
    <a href="#">HR SOLUTIONS</a>
  </nav>
</header>

<section class="abs hero" role="img" aria-label="Blurred bright office interior background"></section>

<div class="abs video">
  <div class="abs" style="inset:0" role="img" aria-label="Video still of a relaxed man leaning back in a chair"></div>
  <p class="abs video-tag">Relaxed!,<br>While we do the job</p>
  <svg class="abs play-ring" width="68" height="68" viewBox="0 0 68 68">
    <circle cx="34" cy="34" r="32" fill="none" stroke="#c41f30" stroke-width="2.5"/>
    <path d="M27 21 L48 34 L27 47 Z" fill="none" stroke="#c41f30" stroke-width="2.5" stroke-linejoin="round"/>
  </svg>
  <div class="abs video-bar">
    <div class="abs play-btn"><svg width="52" height="30"><path d="M21 8 L33 15 L21 22 Z" fill="#fff"/></svg></div>
    <div class="abs track">
      <div class="abs track-fill"><div class="abs track-buffer"></div></div>
      <svg class="abs" style="left:283px;top:8px" width="30" height="10"><g fill="#1e8fe0"><rect x="0" width="2" height="10"/><rect x="4" width="2" height="10"/><rect x="8" width="2" height="10"/><rect x="12" width="2" height="10"/><rect x="16" width="2" height="10"/><rect x="20" width="2" height="10"/></g></svg>
      <span class="abs hd">HD</span>
      <svg class="abs" style="left:346px;top:8px" width="10" height="10"><path d="M0 0 H4 M0 0 V4 M10 0 H6 M10 0 V4 M0 10 H4 M0 10 V6 M10 10 H6 M10 10 V6 M1 1 L9 9 M9 1 L1 9" stroke="#fff" stroke-width="1.6"/></svg>
    </div>
  </div>
</div>

<aside class="abs about-panel">
  <h2 class="abs about-title">WE ARE A DIFFERENT KINF OF AGENCY</h2>
  <div class="abs about-rule"></div>
  <div class="abs about-photo" role="img" aria-label="Photo of a smiling businesswoman with colleagues behind her"></div>
  <p class="abs about-text">
    <span>Mesa Ridge HR Consulting, LLC. (MRHRC) is an</span>
    <span>experienced consulting agency that is committed to</span>
    <span>providing businesses with effective and efficient</span>
    <span>Human Resources support by developing partner-</span>
    <span>ships to meet company's individual needs.</span>
  </p>
  <div class="abs about-tags"><span>EFFECTIVE</span><i>✣</i><span>EXPERIENCED</span><i>✣</i><span>EFFICIENT</span></div>
</aside>

<section>
  <div class="abs divider" style="left:399px"></div>
  <div class="abs divider" style="left:591px"></div>
  <div class="abs divider" style="left:797px"></div>

  <article class="abs feature" style="left:223px">
    <h3>SERVICE AREAS</h3>
    <svg class="icon" width="78" height="78" viewBox="0 0 78 78"><circle cx="39" cy="39" r="37" fill="none" stroke="#c41f30" stroke-dasharray="3 2"/><circle cx="39" cy="39" r="31" fill="#c41f30"/><path d="M25 53 L49 29 M46 24 L54 32" stroke="#fff" stroke-width="5" stroke-linecap="round"/></svg>
    <p>Maecenas eu placerat ante. Fusce ut neque justo, et aliquet enim. In hac habitasse platea dictumst. Nullam commodo neque erat, vitae facilisis erat.</p>
    <span class="learn">LEARN MORE</span>
  </article>

  <article class="abs feature" style="left:417px">
    <h3>THOUGHT LEADERSHIP</h3>
    <svg class="icon" width="78" height="78" viewBox="0 0 78 78"><circle cx="39" cy="39" r="37" fill="none" stroke="#c41f30" stroke-dasharray="3 2"/><circle cx="39" cy="39" r="31" fill="#3a3a3a"/><path d="M24 33 L30 25 H48 L54 33 L39 54 Z M24 33 H54" fill="none" stroke="#fff" stroke-width="2.5" stroke-linejoin="round"/></svg>
    <p>Maecenas eu placerat ante. Fusce ut neque justo, et aliquet enim. In hac habitasse platea dictumst. Nullam commodo neque erat, vitae facilisis erat.</p>
    <span class="learn">LEARN MORE</span>
  </article>

  <article class="abs feature" style="left:615px">
    <h3>HR SOLUTIONS</h3>
    <svg class="icon" width="78" height="78" viewBox="0 0 78 78"><circle cx="39" cy="39" r="37" fill="none" stroke="#c41f30" stroke-dasharray="3 2"/><circle cx="39" cy="39" r="31" fill="#3a3a3a"/><rect x="28" y="24" width="22" height="30" rx="2" fill="#fff"/><path d="M32 32 H46 M32 38 H46 M32 44 H42" stroke="#3a3a3a" stroke-width="2"/></svg>
    <div class="links">
      <div>HR solution for the <b>PUBLIC SECTOR</b></div>
      <div>HR solution for the <b>CORPORATE</b></div>
      <div><b>ROLE BASED</b> HR solution for the</div>
    </div>
    <span class="learn">LEARN MORE</span>
  </article>

  <article class="abs feature" style="left:827px">
    <h3>NEWS &amp; MEDIA</h3>
    <svg class="icon" width="78" height="78" viewBox="0 0 78 78"><circle cx="39" cy="39" r="37" fill="none" stroke="#c41f30" stroke-dasharray="3 2"/><circle cx="39" cy="39" r="31" fill="#3a3a3a"/><circle cx="39" cy="39" r="15" fill="none" stroke="#fff" stroke-width="3"/><circle cx="39" cy="39" r="7" fill="none" stroke="#fff" stroke-width="3"/><path d="M39 18 V60 M18 39 H60" stroke="#fff" stroke-width="2.5"/></svg>
    <p>Maecenas eu placerat ante. Fusce ut neque justo, et aliquet enim. In hac habitasse platea dictumst. Nullam commodo neque erat, vitae facilisis erat.</p>
    <span class="learn">LEARN MORE</span>
  </article>
</section>

<section class="abs band"></section>

<figure class="abs quote">
  <div class="abs quote-photo" role="img" aria-label="Portrait photo of the client giving the testimonial"></div>
  <blockquote class="abs quote-text">Maecenas eu placerat ante. Fusce ut neque justo, et aliquet enim. In hac habitasse platea dictumst. Nullam commodo neque erat, vitae facilisis erat.Maecenas eu placerat ante. Fusce ut neque justo, et aliquet enim. In hac habitasse platea dictumst. Nullam commodo neque erat, vitae facilisis erat.</blockquote>
  <figcaption class="abs quote-by"><b>Sam Ortega /</b>14 Mar 2050 @ 11:07am</figcaption>
</figure>

<h3 class="abs clients-title">OUR SUCCESSFUL CLIENTS</h3>
<svg class="abs arrow" style="left:658px" width="28" height="28"><circle cx="14" cy="14" r="13" fill="#fff"/><path d="M16 8 L10 14 L16 20" fill="none" stroke="#bbb" stroke-width="3"/></svg>
<div class="abs clients-box"><div class="clients-inner">Brightloop Studios</div></div>
<svg class="abs arrow" style="left:947px" width="28" height="28"><circle cx="14" cy="14" r="13" fill="#fff"/><path d="M12 8 L18 14 L12 20" fill="none" stroke="#bbb" stroke-width="3"/></svg>

<div class="abs zig"></div>

<footer class="abs footer">
  <div class="abs foot-col" style="left:230px;top:23px;width:216px">
    <h4>ABOUT US</h4>
    <ul class="foot-list">
      <li>Frequently Asked Questions</li>
      <li>HR Services</li>
      <li>Carrer with us</li>
      <li>Why Choose Us</li>
      <li>Our Company</li>
    </ul>
  </div>
  <div class="abs foot-col" style="left:499px;top:23px;width:208px">
    <h4>CONTACT US</h4>
    <ul class="foot-list contact">
      <li><svg width="12" height="9"><rect width="12" height="9" rx="1" fill="#fff"/><path d="M0 0 L6 5 L12 0" fill="none" stroke="#2a2a2a" stroke-width="1.3"/></svg>info@mesaridgehr.example</li>
      <li><svg width="12" height="12"><path d="M2 1 L5 1 L6 4 L4 5 Q5 8 7 8 L8 6 L11 7 L11 10 Q5 11 1 4 Z" fill="#fff"/></svg>(555) 014-2290</li>
      <li style="height:auto;line-height:19px"><svg width="12" height="14"><path d="M6 0 A5 5 0 0 1 11 5 C11 9 6 14 6 14 C6 14 1 9 1 5 A5 5 0 0 1 6 0 Z" fill="#fff"/><circle cx="6" cy="5" r="2" fill="#2a2a2a"/></svg><span>MRHRC, LLC.<br>P.O. Box 40210<br>Riverton, NM 87000</span></li>
    </ul>
  </div>
  <div class="abs foot-col" style="left:818px;top:23px;width:260px">
    <h4>GET SOCIAL</h4>
    <div class="social">
      <span>Flit</span><span>Kinbook</span><span>Workweb</span>
      <span><svg width="18" height="13"><rect width="18" height="13" rx="1" fill="#222"/><path d="M0 0 L9 7 L18 0" fill="none" stroke="#fff" stroke-width="1.5"/></svg></span>
    </div>
  </div>
</footer>

<div class="abs copy">Mesa Ridge HR Consulting, LLC, All rights reserved</div>

</body>
</html>
```